**URGENT // ENVIRONMENTAL // QUICK TURN AROUND**

We are looking for an A-Grade designer to work with longterm, starting with the successful design for our website & logo; Pelham Grove.

Pelham Grove is a business that focusses on grouping environmentally conscious people together and helping them get "bulk buy" discounts by purchasing large volumes together; solar, energy efficency, wind turbines, and the like.

The Logo and website must have a green feel, as we are here to protect the environment, whilst also helping our customers save money.

The website must also have a blog feature, allowing us to post and keep people up to date with the latest in the industry.

Target Market(s)

FAMILIES WITHIN REGIONAL AUSTRALIA WANTING TO EITHER SAVE MONEY ON ELECTRICITY BILLS, OR REDUCE CARBON EMISSIONS.

Industry/Entity Type

Solar Energy

Logo Text

PELHAM GROVE

Number of Pages Required

5+ page

Font styles to use
Serif
Sans Serif

Colors

Designer to choose colors to be used in the design.

Requirements
Must have
• 1.HOME PAGE
• 2.OUR SERVICES PAGE
• - RENEWABLE ENERGY
• - LIGHTING SYSTEMS
• - ENERGY ASSESSMENT
• - R.G.L.C SCHEME
• - ENERGY COMPARISON
• 4. BOOK AN APPOINTMENT
• 5. IN THE NEWS
• 6. SUBSCRIBE TO NEWSLETTER
• 7. CONTACT US
• MUST LOOK VERY PROFESSIONAL, WITH LOTS OF INFORMATION, IT CANNOT BE BARE AND SIMPLE.
• Can use www.marlowfieldtrading.com.au which is our other brand for copy and ideas - HOWEVER, THIS IS THE REASON WE ARE RE-BRANDING, AS THIS BRAND HAS COME UNDER FAR TOO MUCH CRITICISM FOR LACK OF INFORMATION AND LOOKING TO SIMPLE.
Nice to have
• BLOG FEATURE
Should not have
• ANYTHING THAT APPEARS NON-ENVIRONMENTALS

```html
<!DOCTYPE html>
<html lang="en">
<head>
<meta charset="utf-8">
<title>Pelham Grove</title>
<link rel="stylesheet" href="https://fonts.googleapis.com/css2?family=Poppins:wght@400;500;600;700&family=Roboto+Condensed:wght@400;700&family=Open+Sans:wght@400;600&display=swap">
<style>
:root{
  --green:#4f9a0c;
  --green-bright:#5cb318;
  --green-line:#43b02a;
  --ink:#222222;
  --text:#555555;
  --white:#ffffff;
  --blue-deep:#2e8fe0;
  --blue-light:#9ad2f7;
  --footer:#1d1d1d;
  --footer-text:#d8d8d8;
}
*{margin:0;padding:0;box-sizing:border-box}
html,body{width:1200px;height:2571px;overflow:hidden}
body{position:relative;background:var(--white);font-family:'Open Sans',sans-serif;color:var(--text)}
.abs{position:absolute}

/* header */
.topline{left:0;top:0;width:1200px;height:4px;background:var(--green-line)}
.phone-tab{left:917px;top:0;width:183px;height:36px;background:var(--green-line);border-radius:0 0 28px 28px;color:var(--white);font:600 17px 'Open Sans',sans-serif;display:flex;align-items:center;justify-content:center;gap:10px}
.logo{left:106px;top:40px;display:flex;align-items:center;gap:12px}
.logo-dot{width:30px;height:30px;border-radius:50%;background:var(--green-bright)}
.logo-name{font:700 36px 'Poppins',sans-serif;color:var(--ink);letter-spacing:.5px}
.nav{top:57px;left:597px;display:flex;align-items:center;gap:24px;font:500 14px 'Poppins',sans-serif;color:var(--ink)}
.nav a{color:inherit;text-decoration:none}
.nav .active{background:var(--green-line);color:var(--white);border-radius:16px;padding:6px 22px}

/* hero */
.hero{left:0;top:111px;width:1200px;height:523px;background:linear-gradient(180deg,#aab8c4 0%,#6f8a60 38%,#4d6b3e 55%,#3a4656 75%,#27303d 100%)}
.hero-title{left:98px;top:290px;font:600 48px 'Roboto Condensed',sans-serif;color:var(--white)}
.hero-sub{left:98px;top:353px;width:380px;font:600 13.5px/20px 'Open Sans',sans-serif;color:var(--white)}
.hero-btn{left:98px;top:408px;width:200px;height:41px;border-radius:22px;background:var(--green-bright);border:2px solid #a6e06a;color:var(--white);font:500 15px 'Poppins',sans-serif;display:flex;align-items:center;justify-content:center}
.hero-arrow{top:358px;width:34px;height:34px;border-radius:50%;background:rgba(0,0,0,.55);display:flex;align-items:center;justify-content:center}

/* service cards */
.card{top:569px;width:321px;height:357px;background:var(--green);border:2px solid var(--white);box-shadow:0 2px 6px rgba(0,0,0,.15);color:var(--white);text-align:center}
.card-photo{width:100%;height:194px}
.card-icon{position:absolute;left:50%;top:164px;margin-left:-32px;width:64px;height:64px;border-radius:50%;background:var(--white);border:4px solid var(--green);display:flex;align-items:center;justify-content:center}
.card h3{margin-top:46px;font:500 20px 'Poppins',sans-serif}
.card p{margin:12px 18px 0;font:400 12px/21px 'Open Sans',sans-serif}

/* welcome */
.welcome-title{left:0;top:1008px;width:1200px;text-align:center;font:600 36px 'Poppins',sans-serif;color:var(--ink)}
.welcome-text{left:146px;top:1066px;width:908px;text-align:center;font:400 11.5px/21px 'Open Sans',sans-serif;color:var(--text)}
.bulk-btn{left:547px;top:1147px;width:106px;height:34px;background:var(--green);color:var(--white);font:500 13px 'Poppins',sans-serif;display:flex;align-items:center;justify-content:center;border-radius:2px}

/* supplier band */
.supplier{left:0;top:1256px;width:1200px;height:523px;background:linear-gradient(90deg,var(--blue-deep) 0%,#5cb3f0 45%,var(--blue-light) 62%,#5fb0ee 85%,var(--blue-deep) 100%)}
.supplier-art{left:540px;top:1256px;width:660px;height:523px;background:linear-gradient(180deg,rgba(255,255,255,0) 0%,rgba(150,205,110,.28) 55%,rgba(235,205,180,.22) 80%,rgba(255,255,255,0) 100%)}
.supplier-title{left:98px;top:1318px;font:400 32px 'Roboto Condensed',sans-serif;color:var(--white)}
.feature{left:98px;display:flex;gap:20px;color:var(--white)}
.feature-icon{width:76px;height:76px;border-radius:50%;border:2px solid var(--white);display:flex;align-items:center;justify-content:center;flex:none}
.feature h4{font:400 18px 'Roboto Condensed',sans-serif;margin-top:-2px}
.feature p{width:300px;margin-top:8px;font:400 11.5px/21px 'Open Sans',sans-serif}

/* blog */
.blog-title{left:98px;top:1852px;font:400 34px 'Roboto Condensed',sans-serif;color:var(--ink)}
.blog-title span{color:var(--green)}
.blog-nav{left:1076px;top:1862px;display:flex;gap:8px}
.post-photo{top:1933px;width:188px;height:188px;border-radius:50%;border:3px solid #e4e4e4}
.post{top:1940px;width:266px}
.post h5{font:400 15px 'Poppins',sans-serif;color:#444;white-space:nowrap}
.post .date{margin-top:16px;font:italic 400 12px 'Open Sans',sans-serif;color:var(--green)}
.post p{margin-top:8px;font:400 11.5px/21px 'Open Sans',sans-serif;color:var(--text)}
.post .more{margin-top:8px;font:400 12.5px 'Open Sans',sans-serif;color:#333}

/* footer */
.footer{left:0;top:2211px;width:1200px;height:360px;background:var(--footer)}
.foot-head{top:2255px;font:400 18px 'Roboto Condensed',sans-serif;color:var(--white)}
.foot-text{font:400 12.5px/22px 'Open Sans',sans-serif;color:var(--footer-text)}
.contact-row{left:98px;display:flex;gap:18px;align-items:flex-start}
.signup-text{left:408px;top:2294px;width:300px;font:400 11.5px/20px 'Open Sans',sans-serif;color:var(--footer-text)}
.email-input{left:408px;top:2349px;width:286px;height:40px;background:var(--white);font:400 12px 'Open Sans',sans-serif;color:#666;padding:12px 14px}
.subscribe{left:408px;top:2401px;width:100px;height:40px;background:var(--green);color:var(--white);font:600 12.5px 'Open Sans',sans-serif;display:flex;align-items:center;justify-content:center}
.links{left:790px;top:2298px;list-style:none}
.links li{font:400 12.5px/24px 'Open Sans',sans-serif;color:var(--footer-text)}
.social{left:982px;top:2301px;list-style:none}
.social li{display:flex;align-items:center;gap:10px;height:36px;font:400 14px 'Open Sans',sans-serif;color:var(--footer-text)}
.social .dot{width:26px;height:26px;border-radius:50%;border:1.5px solid var(--footer-text)}
.copyright{left:0;top:2529px;width:1200px;text-align:center;font:400 12.5px 'Open Sans',sans-serif;color:var(--footer-text)}
</style>
</head>
<body>

<header>
  <div class="abs topline"></div>
  <div class="abs phone-tab">
    <svg width="18" height="18" viewBox="0 0 24 24" fill="none" stroke="#fff" stroke-width="2"><path d="M5 3h4l2 5-2.5 1.5a11 11 0 0 0 6 6L16 13l5 2v4a2 2 0 0 1-2 2A16 16 0 0 1 3 5a2 2 0 0 1 2-2z"/></svg>
    08 5550 2184
  </div>
  <div class="abs logo"><span class="logo-dot"></span><span class="logo-name">PELHAM GROVE</span></div>
  <nav class="abs nav">
    <a class="active">HOME</a>
    <a>OUR SERVICES</a>
    <a>BOOK AN APPOINTMENT</a>
    <a>CONTACT US</a>
  </nav>
</header>

<section>
  <div class="abs hero" role="img" aria-label="Photo of solar panel rows on a green hillside with wind turbines and mountains"></div>
  <h1 class="abs hero-title">PELHAM GROVE</h1>
  <p class="abs hero-sub">Sed ut perspiciatis unde omnis iste natus error sit voluptatem accusantium doloremque laudantium, totam</p>
  <div class="abs hero-btn">BOOK AN APPOINTMENT</div>
  <div class="abs hero-arrow" style="left:31px"><svg width="14" height="14" viewBox="0 0 14 14"><path d="M9 2 4 7l5 5" stroke="#fff" stroke-width="2.2" fill="none"/></svg></div>
  <div class="abs hero-arrow" style="left:1128px"><svg width="14" height="14" viewBox="0 0 14 14"><path d="M5 2l5 5-5 5" stroke="#fff" stroke-width="2.2" fill="none"/></svg></div>
</section>

<section>
  <div class="abs card" style="left:99px">
    <div class="card-photo" role="img" aria-label="Photo of a technician installing solar panels" style="background:linear-gradient(180deg,#7fb6e8 0%,#3d6fc2 60%,#2a4f9a 100%)"></div>
    <div class="card-icon"><svg width="28" height="28" viewBox="0 0 24 24" fill="none" stroke="#4f9a0c" stroke-width="2"><circle cx="9" cy="9" r="3"/><path d="M9 2v3M9 13v3M2 9h3M13 9h3"/><circle cx="17" cy="17" r="2.5"/><path d="M17 12.5v2M17 19.5v2M12.5 17h2M19.5 17h2"/></svg></div>
    <h3>Solar Consultations</h3>
    <p>Solar panels are a great way to tap into the free power from our Australian sun! With more usable sunlight than any other country in the world</p>
  </div>
  <div class="abs card" style="left:440px">
    <div class="card-photo" role="img" aria-label="Photo of a living room lit with LED ceiling lights" style="background:linear-gradient(180deg,#d9d6d2 0%,#a29a92 55%,#4a403a 100%)"></div>
    <div class="card-icon"><svg width="26" height="26" viewBox="0 0 24 24" fill="none" stroke="#4f9a0c" stroke-width="2"><path d="M9 18h6M10 21h4M12 3a6 6 0 0 0-3.5 10.9V16h7v-2.1A6 6 0 0 0 12 3z"/></svg></div>
    <h3>LED Lighting Installations</h3>
    <p>LED lighting on average uses 90% less power than halogen globes, last for 20+ years and reduce the risk of house fires. Best of all they are FREE*</p>
  </div>
  <div class="abs card" style="left:779px">
    <div class="card-photo" role="img" aria-label="Photo of wind turbines on a green hill under a blue sky" style="background:linear-gradient(180deg,#3f7fd6 0%,#a9cdf0 55%,#5f9a32 80%,#3f7a22 100%)"></div>
    <div class="card-icon"><svg width="28" height="28" viewBox="0 0 24 24" fill="none" stroke="#4f9a0c" stroke-width="2"><path d="M12 3l3 5h-6zM4 18l3-5 3 5zM20 18h-6l3-5z"/><path d="M9 6 6 11M18 11l-3-5M10 20h4"/></svg></div>
    <h3>Energy Assessments</h3>
    <p>Discover how much energy you could be saving after an energy assessment from one of our highly trained professionals. Simply let us know</p>
  </div>
</section>

<section>
  <h2 class="abs welcome-title">WELCOME TO PELHAM GROVE</h2>
  <p class="abs welcome-text">We love power but we love saving it even more! At Marlowfield Trading we are committed to helping Australian customers connect with leading tier-1 suppliers for Solar, LED and other energy saving products. Sed ut perspiciatis unde omnis iste natus error sit voluptatem accusantium doloremque laudantium, totam rem aperiam, eaque ipsa quae ab illo inventore veritatis et quasi architecto beatae vitae dicta sunt explicabo. Nemo enim ipsam voluptatem quia voluptas</p>
  <div class="abs bulk-btn">BULK BUY</div>
</section>

<section>
  <div class="abs supplier"></div>
  <div class="abs supplier-art" role="img" aria-label="Illustration of two hands holding a small green world with renewable energy sources"></div>
  <h2 class="abs supplier-title">PELHAM GROVE SUPPLIER</h2>
  <div class="abs feature" style="top:1397px">
    <div class="feature-icon"><svg width="36" height="36" viewBox="0 0 36 36" fill="none" stroke="#fff" stroke-width="1.6"><path d="M6 14h22l-3 10H3z"/><path d="M10 14l-2 10M16 14l-2 10M22 14l-2 10M5 19h21"/><path d="M14 24v6M9 30h10"/><circle cx="29" cy="7" r="3"/></svg></div>
    <div><h4>Solar Energy</h4><p>Lorem ipsum dolor sit amet, consectetur adipiscing elit, sed do eiusmod tempor incididunt ut labore et dolore magna aliqua. Ut enim ad minim</p></div>
  </div>
  <div class="abs feature" style="top:1509px">
    <div class="feature-icon"><svg width="36" height="36" viewBox="0 0 24 24" fill="none" stroke="#fff" stroke-width="1.6"><path d="M12 3l3 5h-6zM4 18l3-5 3 5zM20 18h-6l3-5z"/><path d="M9 6 6 11M18 11l-3-5M10 20h4"/></svg></div>
    <div><h4>Energy Efficiency</h4><p>Lorem ipsum dolor sit amet, consectetur adipiscing elit, sed do eiusmod tempor incididunt ut labore et dolore magna aliqua. Ut enim ad minim</p></div>
  </div>
  <div class="abs feature" style="top:1629px">
    <div class="feature-icon"><svg width="36" height="36" viewBox="0 0 36 36" fill="none" stroke="#fff" stroke-width="1.6"><circle cx="18" cy="13" r="2"/><path d="M18 11V2M19.7 14l8 4.5M16.3 14l-8 4.5M18 15v18M14 33h8"/></svg></div>
    <div><h4>Wind Turbines</h4><p>Lorem ipsum dolor sit amet, consectetur adipiscing elit, sed do eiusmod tempor incididunt ut labore et dolore magna aliqua. Ut enim ad minim</p></div>
  </div>
</section>

<section>
  <h2 class="abs blog-title">LATEST <span>BLOG</span></h2>
  <div class="abs blog-nav">
    <svg width="10" height="14" viewBox="0 0 10 14"><path d="M7 2 2 7l5 5" stroke="#1f6fb5" stroke-width="2" fill="none"/></svg>
    <svg width="10" height="14" viewBox="0 0 10 14"><path d="M3 2l5 5-5 5" stroke="#1f6fb5" stroke-width="2" fill="none"/></svg>
  </div>
  <div class="abs post-photo" style="left:102px;background:linear-gradient(180deg,#bcd9f2 0%,#d57a4c 50%,#5a8b3a 100%)" role="img" aria-label="Photo of solar panels on a tiled house roof"></div>
  <article class="abs post" style="left:312px">
    <h5>Nulla at diam ornare, aliquam urna</h5>
    <div class="date">JAN 25, 2017</div>
    <p>Nulla at diam ornare, aliquam urna vel, commodo urna. Nam id risus a est luctus consectetur quis eget libero. Suspendisse potenti. Pellentesque habitant morbi tristique senectus</p>
    <div class="more">Read More +</div>
  </article>
  <div class="abs post-photo" style="left:628px;background:linear-gradient(180deg,#8aa0c4 0%,#e0a36c 55%,#c0653a 100%)" role="img" aria-label="Photo of an electricity pylon at sunset"></div>
  <article class="abs post" style="left:841px">
    <h5>Nulla at diam ornare, aliquam urna</h5>
    <div class="date">JAN 25, 2017</div>
    <p>Nulla at diam ornare, aliquam urna vel, commodo urna. Nam id risus a est luctus consectetur quis eget libero. Suspendisse potenti. Pellentesque habitant morbi tristique senectus</p>
    <div class="more">Read More +</div>
  </article>
</section>

<footer>
  <div class="abs footer"></div>
  <h4 class="abs foot-head" style="left:98px">CONTACT US</h4>
  <div class="abs contact-row" style="top:2298px">
    <svg width="14" height="18" viewBox="0 0 14 18" fill="none" stroke="#d8d8d8" stroke-width="1.5"><path d="M7 17s6-6 6-10A6 6 0 0 0 1 7c0 4 6 10 6 10z"/><circle cx="7" cy="7" r="2"/></svg>
    <div class="foot-text">Pelham Grove<br>Larchmere, Ashby Vale, Hollins,</div>
  </div>
  <div class="abs contact-row" style="top:2352px">
    <svg width="16" height="16" viewBox="0 0 24 24" fill="none" stroke="#d8d8d8" stroke-width="1.8"><path d="M5 3h4l2 5-2.5 1.5a11 11 0 0 0 6 6L16 13l5 2v4a2 2 0 0 1-2 2A16 16 0 0 1 3 5a2 2 0 0 1 2-2z"/></svg>
    <div class="foot-text">Phone : +44(0)20 5550 7712</div>
  </div>
  <div class="abs contact-row" style="top:2385px">
    <svg width="16" height="14" viewBox="0 0 16 14" fill="none" stroke="#d8d8d8" stroke-width="1.4"><rect x="1" y="2" width="14" height="10"/><path d="M1 2l7 6 7-6"/></svg>
    <div class="foot-text">admin@pelhamgrove.com</div>
  </div>

  <h4 class="abs foot-head" style="left:408px">SIGN UP TO RECEIVE EMAIL</h4>
  <p class="abs signup-text">Excepteur sint occaecat cupidatat non proident, sunt in culpa qui Nemo enim ipsam voluptatem</p>
  <div class="abs email-input">Enter Name</div>
  <div class="abs subscribe">SUBSCRIBE</div>

  <h4 class="abs foot-head" style="left:790px">QUICK LINKS</h4>
  <ul class="abs links">
    <li>Home</li><li>About Us</li><li>Book an Appointment</li><li>Our Services</li><li>Blog</li><li>Contact Us</li>
  </ul>

  <h4 class="abs foot-head" style="left:982px">SOCIAL</h4>
  <ul class="abs social">
    <li><span class="dot"></span>Friendwall</li>
    <li><span class="dot"></span>Chirper</li>
    <li><span class="dot"></span>Circleplus</li>
    <li><span class="dot"></span>Vidstream</li>
  </ul>

  <p class="abs copyright">Copyright © Pelham Grove 2017. All rights reserved.</p>
</footer>

</body>
</html>
```